Business card design needed

see my website

www.calderwoodandpike.com

I am after a new logo and business card needs to fit in with the website. I like the look of typewriter text - would like this on the website as well if I could!

Industry/Entity Type

Business

Contact Information for Business Card

Calderwood and Pike
Design and Heritage Consultants

Marcia Dowell
Principal

+61 437 690 215
marcia@calderwoodandpike.com

www.calderwoodandpike.com

back of card

Interior Design
Consultancy on Period Home restoration and renovation
Heritage Impact Statements
Conservation Management Plans
Materials Conservation
Historical Research

```html
<!DOCTYPE html>
<html lang="en">
<head>
<meta charset="utf-8">
<title>Calderwood &amp; Pike — Business Card</title>
<link rel="stylesheet" href="https://fonts.googleapis.com/css2?family=Special+Elite&display=swap">
<style>
  :root {
    --card-bg: #272727;
    --ink: #f4f1ea;
    --accent: #6cc3b8;
  }
  html, body {
    margin: 0;
    padding: 0;
    width: 1200px;
    height: 693px;
    overflow: hidden;
    background: var(--card-bg);
  }
  .card {
    position: relative;
    width: 1200px;
    height: 693px;
    background: var(--card-bg);
    color: var(--ink);
    font-family: "Special Elite", "Courier New", monospace;
  }
  .brand-mark {
    position: absolute;
    left: 557px;
    top: 67px;
    width: 90px;
    height: 90px;
  }
  .brand-name {
    position: absolute;
    left: 0;
    top: 196px;
    width: 1200px;
    margin: 0;
    text-align: center;
    font-size: 50px;
    font-weight: 400;
    letter-spacing: 2px;
    line-height: 1;
  }
  .brand-tagline {
    position: absolute;
    left: 0;
    top: 268px;
    width: 1200px;
    margin: 0;
    text-align: center;
    font-size: 29px;
    line-height: 1;
  }
  .rule {
    position: absolute;
    left: 226px;
    width: 752px;
    height: 4px;
  }
  .rule--top { top: 350px; }
  .rule--bottom { top: 610px; }
  .contact {
    position: absolute;
    left: 226px;
    top: 383px;
    margin: 0;
    padding: 0;
    list-style: none;
    font-size: 28px;
    line-height: 51px;
  }
</style>
</head>
<body>
  <main class="card">
    <svg class="brand-mark" viewBox="0 0 90 90" aria-hidden="true">
      <circle cx="45" cy="45" r="45" fill="var(--accent)"/>
    </svg>

    <h1 class="brand-name">CALDERWOOD &amp; PIKE</h1>
    <p class="brand-tagline">design and heritage consultants</p>

    <svg class="rule rule--top" viewBox="0 0 752 4" aria-hidden="true">
      <line x1="0" y1="2" x2="752" y2="2" stroke="var(--ink)" stroke-width="3" stroke-dasharray="14 9.2"/>
    </svg>

    <ul class="contact">
      <li class="contact__name">Marcia Dowell Principal</li>
      <li class="contact__phone">+61 437 690 215</li>
      <li class="contact__email">marcia@calderwoodandpike.com</li>
      <li class="contact__web">www.calderwoodandpike.com</li>
    </ul>

    <svg class="rule rule--bottom" viewBox="0 0 752 4" aria-hidden="true">
      <line x1="0" y1="2" x2="752" y2="2" stroke="var(--ink)" stroke-width="3" stroke-dasharray="14 9.2"/>
    </svg>
  </main>
</body>
</html>
```